Redesign of Engineering firm website

I want a redesign of the torvelpower.com website with the below in mind:

1- the client has a 3 main sectors: Renewable Energy, Process Automation and General Engineering.
2- Home page should show the 3 sectors
3- the other standard pages should be home, About, Clients, Projects, Training, Career, and Contact
4- The theme should be wordpress.
5- Responsive layout that works with all devices
6- One page layout is preferable for the home page.
7- it should be original and is not copied from other templates.
Updates

Reason: As requested from so many designers... the deadline is extended. Thank you

Target Market(s)

Engineers and professional

Industry/Entity Type

Solar Energy

Font styles to use
Serif
Sans Serif

Colors
3277b5
0355a3
0493ce

Requirements
Must have
• pictures that represent the three sectors

```html
<!DOCTYPE html>
<html lang="en">
<head>
<meta charset="utf-8">
<title>Torvel Power Consulting</title>
<link rel="stylesheet" href="https://fonts.googleapis.com/css2?family=Roboto:wght@400;500;700;900&family=Open+Sans:wght@400;600;700&display=swap">
<style>
:root{
  --blue:#0355a3;
  --blue-mid:#3277b5;
  --cyan:#0493ce;
  --ink:#222;
  --text:#555;
  --line:#d9d9d9;
  --white:#fff;
}
*{box-sizing:border-box;margin:0;padding:0}
html,body{width:1200px;height:2605px;overflow:hidden;background:var(--white)}
body{font-family:"Open Sans",sans-serif;color:var(--text);position:relative}
.wrap{width:1006px;margin:0 auto;position:relative}
svg{display:block}

/* header */
.site-header{height:96px;border-top:4px solid var(--blue);position:relative}
.brand{position:absolute;left:97px;top:16px;font-family:"Roboto",sans-serif;font-weight:900;font-size:44px;color:var(--cyan);letter-spacing:-1px}
.top-contact{position:absolute;right:225px;top:12px;display:flex;gap:22px;font-family:"Roboto",sans-serif;font-weight:500;font-size:17px;color:var(--ink)}
.top-contact span{display:flex;align-items:center;gap:10px}
.circle-icon{width:32px;height:32px;border:1.5px solid #bbb;border-radius:50%;display:flex;align-items:center;justify-content:center}
.login{position:absolute;right:97px;top:0;width:108px;height:34px;background:var(--blue);color:#fff;font:700 14px "Roboto",sans-serif;display:flex;align-items:center;justify-content:center;gap:6px;clip-path:polygon(12% 0,100% 0,100% 100%,0 100%)}
.main-nav{position:absolute;right:97px;top:66px;display:flex;gap:21px;font:500 15px "Roboto",sans-serif;color:var(--ink);align-items:center}
.main-nav .active{color:var(--cyan)}

/* hero */
.hero{height:426px;position:relative;text-align:center;color:#fff;background:linear-gradient(180deg,#b99a78 0%,#8c7560 40%,#5b4c3a 70%,#3d3a2f 100%)}
.hero-media{position:absolute;inset:0}
.hero h1{position:relative;padding-top:100px;font:700 57px "Roboto",sans-serif}
.hero-lead{position:relative;margin-top:10px;font-size:20px;line-height:28px}
.btn-hero{position:relative;display:inline-flex;align-items:center;justify-content:center;margin-top:30px;width:180px;height:40px;border-radius:20px;background:var(--cyan);border:2px solid #fff;font:700 15px "Roboto",sans-serif}
.dots{position:relative;margin-top:54px;display:flex;justify-content:center;gap:6px}
.dots i{width:12px;height:12px;border:2px solid #fff;border-radius:50%}
.dots i.on{background:#fff}

/* welcome */
.welcome{text-align:center;padding-top:68px}
.welcome h2{font:700 27px "Roboto",sans-serif;color:var(--ink)}
.welcome-intro{margin:20px auto 0;width:900px;font-size:12.5px;line-height:24px}
.sectors{display:flex;gap:36px;justify-content:center;margin-top:52px}
.sector{width:312px;height:440px;border:2px solid #e1e1e1;box-shadow:0 1px 4px rgba(0,0,0,.08);padding:4px;text-align:center;position:relative}
.sector-photo{height:217px}
.sector-badge{position:absolute;left:50%;top:185px;margin-left:-37px;width:74px;height:74px;border-radius:50%;background:var(--cyan);border:4px solid #fff;display:flex;align-items:center;justify-content:center}
.sector h3{margin-top:52px;font:500 20px "Roboto",sans-serif;color:var(--ink)}
.sector-text{margin:12px 18px 0;width:auto;font-size:12px;line-height:23px;white-space:normal}
.btn-outline{display:inline-flex;align-items:center;justify-content:center;margin-top:20px;width:138px;height:32px;border:1.5px solid #ccc;border-radius:16px;font:700 12px "Open Sans",sans-serif;color:var(--cyan)}

/* projects */
.projects{margin-top:70px;height:462px;background:var(--blue);position:relative;color:#fff;overflow:hidden}
.projects-art{position:absolute;right:0;top:0;width:660px;height:462px}
.projects h2{position:absolute;left:97px;top:44px;font:700 26px "Roboto",sans-serif}
.project-list{position:absolute;left:97px;top:110px;list-style:none}
.project-list li{display:flex;align-items:center;gap:12px;font-size:13px;height:31px}

/* training / career */
.features{display:flex;gap:60px;margin-top:80px}
.feature{display:flex;gap:24px;width:473px}
.feature-photo{flex:0 0 209px;height:180px;border:2px solid #e1e1e1;padding:3px}
.feature-photo div{width:100%;height:100%}
.feature h3{font:700 27px "Roboto",sans-serif;color:var(--ink);margin-top:-2px}
.feature-text{margin-top:14px;font-size:12px;line-height:23px;width:250px}
.feature .btn-outline{margin-top:14px;width:127px}
.divider{border:0;border-top:1px solid var(--line)}

/* clients */
.clients-title{text-align:center;font:700 26px "Roboto",sans-serif;color:var(--ink);margin-top:45px}
.client-row{display:flex;justify-content:space-between;margin-top:34px}
.client{width:178px;height:87px;border:3px solid #e3e3e3;display:flex;align-items:center;justify-content:center;font:600 26px "Open Sans",sans-serif;color:#8a8a8a}

/* footer */
.site-footer{position:absolute;left:0;right:0;top:2316px;border-top:4px solid var(--cyan)}
.footer-contact{display:flex;justify-content:center;gap:56px;margin-top:55px;font:500 15px "Open Sans",sans-serif;color:var(--ink);align-items:center}
.footer-contact span{display:flex;align-items:center;gap:20px;line-height:23px}
.footer-contact .circle-icon{width:50px;height:50px}
.footer-nav{display:flex;justify-content:center;gap:16px;margin-top:40px;font-size:15px;color:var(--ink)}
.footer-bottom{margin-top:30px;padding-top:30px;border-top:1px solid var(--line);display:flex;justify-content:space-between;align-items:center;font-size:13px;color:var(--ink)}
.social{display:flex;gap:8px}
.social i{width:38px;height:38px;border-radius:50%}
</style>
</head>
<body>

<header class="site-header">
  <div class="brand">TORVEL</div>
  <div class="top-contact">
    <span><span class="circle-icon"><svg width="14" height="14" viewBox="0 0 24 24"><path d="M6.6 10.8a15 15 0 0 0 6.6 6.6l2.2-2.2a1 1 0 0 1 1-.25 11.4 11.4 0 0 0 3.6.57 1 1 0 0 1 1 1V20a1 1 0 0 1-1 1A17 17 0 0 1 3 4a1 1 0 0 1 1-1h3.5a1 1 0 0 1 1 1c0 1.25.2 2.45.57 3.57a1 1 0 0 1-.25 1z" fill="#0355a3"/></svg></span>+966135550142</span>
    <span><span class="circle-icon"><svg width="15" height="12" viewBox="0 0 24 18"><rect width="24" height="18" rx="2" fill="#0355a3"/><path d="M1 2l11 8 11-8" stroke="#fff" stroke-width="2" fill="none"/></svg></span>info@torvelpower.com</span>
  </div>
  <div class="login"><svg width="11" height="13" viewBox="0 0 12 14"><rect y="6" width="12" height="8" rx="1" fill="#fff"/><path d="M3 6V4a3 3 0 0 1 6 0v2" stroke="#fff" stroke-width="2" fill="none"/></svg>LOGIN</div>
  <nav class="main-nav">
    <span class="active">HOME</span><span>ABOUT</span><span>CLIENTS</span><span>PROJECTS</span><span>TRAINING</span><span>CAREER</span><span>CONTACT</span>
    <svg width="15" height="15" viewBox="0 0 16 16"><circle cx="6.5" cy="6.5" r="5" stroke="#222" stroke-width="2" fill="none"/><path d="M10.5 10.5l4 4" stroke="#222" stroke-width="2.5"/></svg>
  </nav>
</header>

<section class="hero">
  <div class="hero-media" role="img" aria-label="Photo of wind turbines on a hillside above clouds at sunset"></div>
  <h1>TORVEL POWER CONSULTING</h1>
  <p class="hero-lead">We are the solar experts in the solar kingdom. The KSA (Saudi Arabia)<br>solar market is a promising market with huge potential</p>
  <a class="btn-hero">GET MORE INFO &gt;&gt;</a>
  <div class="dots"><i class="on"></i><i></i><i></i><i></i></div>
</section>

<section class="welcome wrap">
  <h2>WELCOME TO TORVEL POWER CONSULTING</h2>
  <p class="welcome-intro">We are the solar experts in the solar kingdom. The KSA (Saudi Arabia) solar market is a promising market with huge potential. The plan is to build 41,000 MW of solar in the coming 20 years, as announced by S.R.A. (Solarion Renewables Authority). We provide our services, both.</p>
  <div class="sectors">
    <article class="sector">
      <div class="sector-photo" role="img" aria-label="Photo of solar panels and wind turbines under a blue sky" style="background:linear-gradient(180deg,#6fa6d8 0%,#c9def0 45%,#7f8f9c 60%,#33507a 100%)"></div>
      <div class="sector-badge"><svg width="34" height="34" viewBox="0 0 24 24"><circle cx="12" cy="12" r="10" stroke="#fff" stroke-width="1.8" fill="none"/><path d="M13 5l-5 8h4l-1 6 5-8h-4z" fill="#fff"/></svg></div>
      <h3>Renewable Energy</h3>
      <p class="sector-text">Torvel-Solar: provides Solar Energy consulting services, Energy Efficiency Consulting services and Data Collection function.</p>
      <a class="btn-outline">READ MORE &gt;&gt;</a>
    </article>
    <article class="sector">
      <div class="sector-photo" role="img" aria-label="Photo of a hand touching a digital network of automation icons" style="background:linear-gradient(135deg,#dfe9f3 0%,#9fb8cf 45%,#3d5d7e 100%)"></div>
      <div class="sector-badge"><svg width="34" height="34" viewBox="0 0 24 24"><circle cx="9" cy="14" r="5" stroke="#fff" stroke-width="2.5" stroke-dasharray="2.2 1.7" fill="none"/><circle cx="9" cy="14" r="2" fill="#fff"/><circle cx="17" cy="7" r="3.5" stroke="#fff" stroke-width="2" stroke-dasharray="1.6 1.2" fill="none"/></svg></div>
      <h3>Process Automation</h3>
      <p class="sector-text">Torvel-Solar: provides Solar Energy consulting services, Energy Efficiency Consulting services and Data Collection function.</p>
      <a class="btn-outline">READ MORE &gt;&gt;</a>
    </article>
    <article class="sector">
      <div class="sector-photo" role="img" aria-label="Photo of an engineer at a desk with a wind turbine model" style="background:linear-gradient(135deg,#cfc4b6 0%,#a99b89 45%,#e6e6e6 100%)"></div>
      <div class="sector-badge"><svg width="32" height="32" viewBox="0 0 24 24"><rect x="3" y="5" width="14" height="15" rx="2" stroke="#fff" stroke-width="2" fill="none"/><path d="M10 14l9-9 2 2-9 9h-2z" fill="#fff"/></svg></div>
      <h3>General Engineering</h3>
      <p class="sector-text">Torvel-Solar: provides Solar Energy consulting services, Energy Efficiency Consulting services and Data Collection function.</p>
      <a class="btn-outline">READ MORE &gt;&gt;</a>
    </article>
  </div>
</section>

<section class="projects">
  <div class="projects-art" role="img" aria-label="Faint technical line drawing of engineering gears" style="background:radial-gradient(ellipse at 60% 50%,rgba(120,170,230,.55),rgba(3,85,163,0) 70%)"></div>
  <h2>OUR PROJECTS</h2>
  <ul class="project-list">
    <li><svg width="14" height="14" viewBox="0 0 16 16"><circle cx="8" cy="8" r="8" fill="#fff"/><path d="M4.5 8.2l2.3 2.3 4.7-4.7" stroke="#0355a3" stroke-width="2" fill="none"/></svg>Nordvale Institute Energy Efficiency Study for NIEP.</li>
    <li><svg width="14" height="14" viewBox="0 0 16 16"><circle cx="8" cy="8" r="8" fill="#fff"/><path d="M4.5 8.2l2.3 2.3 4.7-4.7" stroke="#0355a3" stroke-width="2" fill="none"/></svg>Solarion Authority Solar Atlas</li>
    <li><svg width="14" height="14" viewBox="0 0 16 16"><circle cx="8" cy="8" r="8" fill="#fff"/><path d="M4.5 8.2l2.3 2.3 4.7-4.7" stroke="#0355a3" stroke-width="2" fill="none"/></svg>Solarion Authority Irradiation data Development</li>
    <li><svg width="14" height="14" viewBox="0 0 16 16"><circle cx="8" cy="8" r="8" fill="#fff"/><path d="M4.5 8.2l2.3 2.3 4.7-4.7" stroke="#0355a3" stroke-width="2" fill="none"/></svg>Coastline University Digital Energy meter for Residential campus</li>
    <li><svg width="14" height="14" viewBox="0 0 16 16"><circle cx="8" cy="8" r="8" fill="#fff"/><path d="M4.5 8.2l2.3 2.3 4.7-4.7" stroke="#0355a3" stroke-width="2" fill="none"/></svg>Embassy Row District Energy Data consumption</li>
    <li><svg width="14" height="14" viewBox="0 0 16 16"><circle cx="8" cy="8" r="8" fill="#fff"/><path d="M4.5 8.2l2.3 2.3 4.7-4.7" stroke="#0355a3" stroke-width="2" fill="none"/></svg>Westmere Hospital Energy Efficiency</li>
    <li><svg width="14" height="14" viewBox="0 0 16 16"><circle cx="8" cy="8" r="8" fill="#fff"/><path d="M4.5 8.2l2.3 2.3 4.7-4.7" stroke="#0355a3" stroke-width="2" fill="none"/></svg>Altura Global Solar analysis support for GCC new installation</li>
    <li><svg width="14" height="14" viewBox="0 0 16 16"><circle cx="8" cy="8" r="8" fill="#fff"/><path d="M4.5 8.2l2.3 2.3 4.7-4.7" stroke="#0355a3" stroke-width="2" fill="none"/></svg>Electrical Grounding Courses</li>
    <li><svg width="14" height="14" viewBox="0 0 16 16"><circle cx="8" cy="8" r="8" fill="#fff"/><path d="M4.5 8.2l2.3 2.3 4.7-4.7" stroke="#0355a3" stroke-width="2" fill="none"/></svg>Meridian Research Center projects as references (4) projects</li>
    <li><svg width="14" height="14" viewBox="0 0 16 16"><circle cx="8" cy="8" r="8" fill="#fff"/><path d="M4.5 8.2l2.3 2.3 4.7-4.7" stroke="#0355a3" stroke-width="2" fill="none"/></svg>Developing Short Video clips for events and illustrating engineering concepts</li>
  </ul>
</section>

<section class="wrap">
  <div class="features">
    <article class="feature">
      <div class="feature-photo"><div role="img" aria-label="Photo of metal gears on a pale blue technical sheet" style="background:linear-gradient(135deg,#e8f3f8 0%,#a9cfe0 55%,#5f93ad 100%)"></div></div>
      <div>
        <h3>TRAINING</h3>
        <p class="feature-text">We cover all technology, market and finance related aspects of solar PV. Our network of government officials, real estate experts, market analyst, and industry..</p>
        <a class="btn-outline">READ MORE &gt;&gt;</a>
      </div>
    </article>
    <article class="feature">
      <div class="feature-photo"><div role="img" aria-label="Photo of a professional seated at a desk in an office" style="background:linear-gradient(135deg,#d7c7a6 0%,#8d7a5e 50%,#2f2a26 100%)"></div></div>
      <div>
        <h3>CAREER</h3>
        <p class="feature-text">We cover all technology, market and finance related aspects of solar PV. Our network of government officials, real estate experts, market analyst, and industry..</p>
        <a class="btn-outline">READ MORE &gt;&gt;</a>
      </div>
    </article>
  </div>
  <hr class="divider" style="margin-top:68px">
  <h2 class="clients-title">OUR CLIENTS</h2>
  <div class="client-row">
    <div class="client">Brisk</div>
    <div class="client">Envoya</div>
    <div class="client">Quentara</div>
    <div class="client">Liftwise</div>
    <div class="client">Studyway</div>
  </div>
</section>

<footer class="site-footer">
  <div class="footer-contact">
    <span><span class="circle-icon"><svg width="16" height="22" viewBox="0 0 16 22"><path d="M8 1a7 7 0 0 0-7 7c0 5 7 13 7 13s7-8 7-13a7 7 0 0 0-7-7z" stroke="#0355a3" stroke-width="2" fill="none"/><circle cx="8" cy="8" r="2.5" fill="#0355a3"/></svg></span>Harbor Road, Eastern Province 34417<br>Kingdom of Saudi Arabia</span>
    <span><span class="circle-icon"><svg width="18" height="18" viewBox="0 0 24 24"><path d="M6.6 10.8a15 15 0 0 0 6.6 6.6l2.2-2.2a1 1 0 0 1 1-.25 11.4 11.4 0 0 0 3.6.57 1 1 0 0 1 1 1V20a1 1 0 0 1-1 1A17 17 0 0 1 3 4a1 1 0 0 1 1-1h3.5a1 1 0 0 1 1 1c0 1.25.2 2.45.57 3.57a1 1 0 0 1-.25 1z" fill="#0355a3"/></svg></span>+966135550142</span>
    <span><span class="circle-icon"><svg width="20" height="15" viewBox="0 0 24 18"><rect width="24" height="18" rx="2" fill="#0355a3"/><path d="M1 2l11 8 11-8" stroke="#fff" stroke-width="2" fill="none"/></svg></span>info@torvelpower.com</span>
  </div>
  <nav class="footer-nav">
    <span>Home</span><span>|</span><span>About</span><span>|</span><span>Clients</span><span>|</span><span>Projects</span><span>|</span><span>Training</span><span>|</span><span>Career</span><span>|</span><span>Contact</span>
  </nav>
  <div class="wrap footer-bottom">
    <span>Copyright 2017. Torvel Power Consulting All rights reserved.</span>
    <div class="social"><i style="background:#2d5a8c"></i><i style="background:#3aaee0"></i><i style="background:#e2574c"></i></div>
  </div>
</footer>

</body>
</html>
```